New Wix logo and website layout

I need a new logo design and a new, modern website layout design. I am a professional therapist providing remedial massage. I am Canadian but live in Australia & would like the logo to have a somewhat 'Canadian feel' to it (something subtle i.e. no flags) I currently have a maple tree leaf as my logo. my current website is stonebaymassage.com.au. I need the website to work on mobile phones & traditional web browsers.

Target Market(s)

customers looking for remedial massage and manual lymphatic drainage

Industry/Entity Type

professional massage

Coding

Coded - Design and coding required

Font styles to use
Sans Serif

Colors
EB3D1F
EC4F4E
F09395
F8D3D4
FCEDEE

Requirements
Nice to have
• something subtle that indicates that I am canadian
Should not have
• no flags. nothing too bold

```html
<!DOCTYPE html>
<html lang="en">
<head>
<meta charset="utf-8">
<title>Stone Bay Massage</title>
<link rel="stylesheet" href="https://fonts.googleapis.com/css2?family=Cinzel:wght@400;700&family=Lato:wght@400;700;900&display=swap">
<style>
:root{
  --red:#EB3D1F;
  --coral:#EC4F4E;
  --pink:#F09395;
  --blush:#F8D3D4;
  --mist:#FCEDEE;
  --ink:#3a3a3a;
  --dark:#1e1c1c;
  --white:#ffffff;
}
*{box-sizing:border-box;margin:0;padding:0}
html,body{width:1200px;height:3740px;overflow:hidden}
body{position:relative;background:var(--white);font-family:"Lato",sans-serif;color:var(--ink)}
.abs{position:absolute}

/* header */
.site-header{position:absolute;left:0;top:0;width:1200px;height:120px;z-index:5}
.brand{position:absolute;left:140px;top:34px;display:flex;align-items:center;gap:12px;font-family:"Lato",sans-serif;font-weight:900;font-size:30px;color:var(--red);letter-spacing:1px}
.brand-dot{width:22px;height:22px;border-radius:50%;background:var(--red)}
.header-phone{position:absolute;right:140px;top:14px;display:flex;align-items:center;gap:12px;font-size:34px;font-weight:700;color:var(--red)}
.header-phone .icon{width:36px;height:36px;border-radius:50%;background:var(--red);display:flex;align-items:center;justify-content:center}
.main-nav{position:absolute;left:480px;top:66px;display:flex;gap:34px;align-items:center;font-size:15px;font-weight:900;color:#333;letter-spacing:.5px}
.main-nav .active{color:var(--red)}

/* hero */
.hero-photo{position:absolute;left:0;top:0;width:1200px;height:860px;background:linear-gradient(100deg,#f4ebe3 0%,#efd9c8 45%,#e8c3a8 70%,#f2e3d8 100%)}
.hero-badge{position:absolute;left:128px;top:280px;width:320px;height:320px;border-radius:50%;background:var(--red);display:flex;flex-direction:column;align-items:center;justify-content:center;text-align:center;box-shadow:0 0 0 10px rgba(255,255,255,.55)}
.hero-badge h1{font-family:"Cinzel",serif;font-weight:700;font-size:40px;line-height:1.1;color:var(--white);margin-top:20px}
.btn{display:inline-block;border-radius:30px;font-family:"Lato",sans-serif;font-weight:900;font-size:14px;letter-spacing:1px;text-transform:uppercase}
.btn-light{background:var(--white);color:var(--red);padding:14px 24px;margin-top:26px}
.btn-red{background:var(--coral);color:var(--white);padding:16px 30px}
.hero-wave{position:absolute;left:0;top:700px;width:1200px;height:200px}

/* about */
.section-title{font-family:"Cinzel",serif;font-weight:400;color:#222;line-height:1.1}
.about-title{position:absolute;left:144px;top:836px;font-size:56px}
.rule{height:3px;width:120px;background:var(--red)}
.about-rule{position:absolute;left:144px;top:912px}
.about-text{position:absolute;left:144px;top:944px;width:540px;font-size:16px;line-height:1.75;color:#555}
.about-text p+p{margin-top:14px}
.about-btn{position:absolute;left:144px;top:1216px}
.portrait-ring{position:absolute;left:710px;top:838px;width:340px;height:340px;border-radius:50%;background:var(--red);padding:10px}
.portrait{width:100%;height:100%;border-radius:50%;background:radial-gradient(circle at 50% 40%,#f3d7c2 0%,#d9a676 55%,#b98a5e 100%)}

/* services */
.service{position:absolute;overflow:hidden}
.service-photo{width:100%;height:100%}
.service-label{position:absolute;left:0;bottom:0;width:100%;height:44px;background:var(--red);color:var(--white);font-weight:900;font-size:28px;text-align:center;line-height:44px;letter-spacing:.5px;text-transform:uppercase}

/* remedial */
.remedial-photo{position:absolute;left:0;top:2040px;width:600px;height:560px;background:linear-gradient(180deg,#ffffff 0%,#f6eee9 40%,#e7cdbd 75%,#6f4b3a 100%)}
.remedial-title{position:absolute;left:600px;top:2080px;font-size:56px}
.remedial-rule{position:absolute;left:600px;top:2226px}
.remedial-text{position:absolute;left:600px;top:2252px;width:460px;font-size:16px;line-height:1.75;color:#555;text-align:justify}
.remedial-btn{position:absolute;left:600px;top:2496px}

/* contact */
.leaf-photo{position:absolute;left:520px;top:2600px;width:680px;height:780px;background:radial-gradient(ellipse at 45% 30%,#f07a2a 0%,#e0531e 30%,#f2b48e 60%,#ffffff 85%)}
.wave-band{position:absolute;left:0;top:2540px;width:1200px;height:260px}
.contact-title{position:absolute;left:144px;top:2900px;font-size:56px}
.contact-form{position:absolute;left:144px;top:3012px;width:600px}
.field{background:var(--white);border:1px solid #ddd;height:52px;font-size:14px;color:#777;padding:0 18px;line-height:52px;box-shadow:0 2px 6px rgba(0,0,0,.08)}
.row{display:flex;gap:16px;margin-bottom:18px}
.row .field{flex:1}
.field.message{height:96px;line-height:1;padding-top:18px;margin-bottom:28px}
.btn-submit{background:var(--coral);color:var(--white);padding:18px 36px}

/* footer */
.footer-shape{position:absolute;left:0;top:3320px;width:1200px;height:420px}
.footer-contact{position:absolute;left:752px;top:3436px;color:var(--white)}
.footer-contact h2{font-family:"Cinzel",serif;font-weight:400;font-size:52px;margin-bottom:22px}
.contact-line{display:flex;gap:20px;align-items:flex-start;font-size:17px;line-height:1.5;margin-bottom:10px}
.contact-line svg{flex:none;margin-top:4px}
.footer-nav{position:absolute;left:144px;top:3580px;display:flex;gap:30px;font-size:15px;font-weight:900;color:var(--white)}
.copyright{position:absolute;left:144px;top:3624px;font-size:13px;color:#cfcfcf}
.social{position:absolute;left:144px;top:3664px;display:flex;gap:16px}
.social span{width:34px;height:34px;border-radius:50%;background:var(--red)}
</style>
</head>
<body>

<div class="hero-photo" role="img" aria-label="Photo of a woman relaxing during a back massage"></div>

<header class="site-header">
  <div class="brand"><span class="brand-dot"></span>Stone Bay Massage</div>
  <div class="header-phone">
    <span class="icon"><svg width="18" height="18" viewBox="0 0 24 24"><path fill="#fff" d="M6.6 10.8a15.2 15.2 0 0 0 6.6 6.6l2.2-2.2c.3-.3.7-.4 1-.2 1.1.4 2.3.6 3.6.6.6 0 1 .4 1 1V20c0 .6-.4 1-1 1A17 17 0 0 1 3 4c0-.6.4-1 1-1h3.5c.6 0 1 .4 1 1 0 1.3.2 2.5.6 3.6.1.3 0 .7-.2 1z"/></svg></span>
    0400 517 268
  </div>
  <nav class="main-nav">
    <span class="active">HOME</span><span>REMEDIAL MASSAGE</span><span>ABOUT ME</span><span>FEES</span><span>CONTACT</span>
    <svg width="18" height="18" viewBox="0 0 24 24"><circle cx="10" cy="10" r="7" fill="none" stroke="#EB3D1F" stroke-width="3"/><path d="M15 15l6 6" stroke="#EB3D1F" stroke-width="3" stroke-linecap="round"/></svg>
  </nav>
</header>

<div class="hero-badge">
  <h1>STONE BAY<br>MASSAGE</h1>
  <span class="btn btn-light">Get Started</span>
</div>

<svg class="hero-wave" viewBox="0 0 1200 200" preserveAspectRatio="none">
  <path d="M0 60 C300 200 800 200 1200 40 L1200 200 L0 200Z" fill="#fff"/>
  <path d="M0 60 C300 200 800 200 1200 40" fill="none" stroke="#EB3D1F" stroke-width="8"/>
  <path d="M0 90 C320 210 820 200 1200 80" fill="none" stroke="#F09395" stroke-width="3"/>
</svg>

<h2 class="section-title about-title">ABOUT ME</h2>
<div class="rule about-rule"></div>
<div class="about-text">
  <p>I completed my training in Toronto, Canada in 1999 where I obtained a Diploma of Remedial Massage through the Northern College of Massage Therapy.</p>
  <p>Over the years, I have practiced in several different settings including medical centre, chiropractic clinic, spa and currently am a sole trader in my own practice. I have been helping my clients achieve better health through my treatments for several years. I take special interest in women's health.</p>
</div>
<span class="btn btn-red about-btn">Read More</span>
<div class="portrait-ring"><div class="portrait" role="img" aria-label="Portrait photo of the therapist"></div></div>

<div class="service" style="left:0;top:1340px;width:396px;height:332px">
  <div class="service-photo" role="img" aria-label="Photo of a remedial massage treatment" style="background:linear-gradient(160deg,#f3ede8,#d9b89c)"></div>
  <div class="service-label">Remedial</div>
</div>
<div class="service" style="left:402px;top:1340px;width:398px;height:332px">
  <div class="service-photo" role="img" aria-label="Photo of a deep tissue massage on the shoulder" style="background:linear-gradient(160deg,#e6c6ae,#b98566)"></div>
  <div class="service-label">Deep Tissue</div>
</div>
<div class="service" style="left:806px;top:1340px;width:394px;height:332px">
  <div class="service-photo" role="img" aria-label="Photo of a therapeutic arm massage" style="background:linear-gradient(160deg,#f1e9e3,#cfae98)"></div>
  <div class="service-label">Therapeutic</div>
</div>
<div class="service" style="left:0;top:1680px;width:596px;height:340px">
  <div class="service-photo" role="img" aria-label="Photo of a pregnancy massage" style="background:linear-gradient(160deg,#d8b393,#8a5c3e)"></div>
  <div class="service-label">Pregnancy</div>
</div>
<div class="service" style="left:604px;top:1680px;width:596px;height:340px">
  <div class="service-photo" role="img" aria-label="Photo of lymphatic drainage massage on the leg" style="background:linear-gradient(160deg,#e7b795,#b5704b)"></div>
  <div class="service-label">Lymphatic Drainage</div>
</div>

<div class="remedial-photo" role="img" aria-label="Photo of a therapist preparing to massage a client lying on a table"></div>
<h2 class="section-title remedial-title">REMEDIAL<br>MASSAGE</h2>
<div class="rule remedial-rule"></div>
<p class="remedial-text">Remedial massage is used to help relieve tension and stress in the soft tissues of the body including muscles, tendons, ligaments and connective tissue. It helps to alleviate soft tissue discomfort associated with everyday and occupational stress, over-use injuries e.g. tendinitis, and many chronic pain conditions. An increase in circulation and increased joint flexibility are additional benefits.</p>
<span class="btn btn-red remedial-btn">Read More</span>

<div class="leaf-photo" role="img" aria-label="Photo of a red autumn leaf reflected in water"></div>
<svg class="wave-band" viewBox="0 0 1200 260" preserveAspectRatio="none">
  <path d="M0 110 C260 10 480 20 620 70 C800 140 980 150 1200 80 L1200 0 L0 0Z" fill="#fff"/>
  <path d="M0 110 C260 10 480 20 620 70 C800 140 980 150 1200 80" fill="none" stroke="#EB3D1F" stroke-width="10"/>
  <path d="M0 140 C260 40 480 50 620 100 C800 170 980 180 1200 110" fill="none" stroke="#EC4F4E" stroke-width="4"/>
</svg>

<h2 class="section-title contact-title">CONTACT</h2>
<div class="rule" style="position:absolute;left:144px;top:2972px;width:100px"></div>
<form class="contact-form">
  <div class="row"><div class="field">Enter Name</div><div class="field">Enter Email</div></div>
  <div class="row"><div class="field">Phone</div><div class="field">Address</div></div>
  <div class="field message">Message</div>
  <span class="btn btn-submit">Submit</span>
</form>

<svg class="footer-shape" viewBox="0 0 1200 420" preserveAspectRatio="none">
  <path d="M0 160 C400 150 800 80 1200 20 L1200 420 L0 420Z" fill="#1e1c1c"/>
</svg>

<div class="footer-contact">
  <h2>CONTACT</h2>
  <div class="contact-line">
    <svg width="20" height="26" viewBox="0 0 20 26"><path d="M10 0a10 10 0 0 0-10 10c0 7 10 16 10 16s10-9 10-16A10 10 0 0 0 10 0z" fill="#EB3D1F"/><circle cx="10" cy="10" r="4" fill="#1e1c1c"/></svg>
    <span>Dana Reid<br>24 Harbour Lane<br>Seaford VIC 3198</span>
  </div>
  <div class="contact-line">
    <svg width="20" height="20" viewBox="0 0 24 24"><path fill="#EB3D1F" d="M6.6 10.8a15.2 15.2 0 0 0 6.6 6.6l2.2-2.2c.3-.3.7-.4 1-.2 1.1.4 2.3.6 3.6.6.6 0 1 .4 1 1V20c0 .6-.4 1-1 1A17 17 0 0 1 3 4c0-.6.4-1 1-1h3.5c.6 0 1 .4 1 1 0 1.3.2 2.5.6 3.6.1.3 0 .7-.2 1z"/></svg>
    <span>0400 517 268</span>
  </div>
  <div class="contact-line">
    <svg width="20" height="16" viewBox="0 0 20 16"><rect width="20" height="16" rx="2" fill="#EB3D1F"/><path d="M1 2l9 7 9-7" fill="none" stroke="#1e1c1c" stroke-width="2"/></svg>
    <span>dana@stonebaymassage.com.au</span>
  </div>
</div>

<nav class="footer-nav"><span>HOME</span><span>REMEDIAL MASSAGE</span><span>ABOUT ME</span><span>FEES</span><span>CONTACT</span></nav>
<p class="copyright">© 2022 Stone Bay Massage. All rights reserved Privacy | Terms of Use</p>
<div class="social"><span></span><span></span><span></span></div>

</body>
</html>
```